Logo and Simple Website - Orbly IT

I require a good logo and simple website for an IT trading business. I am uploading the website text and description.
For the logo, I was thinking of something that has a (partial) cube but also looks a bit like a circuit board. The name should be easy to read, but there should also be a graphical element to the logo. The graphical element can be used on its own for tabs or headers on the website. The logo needs to be suitable for business cards and stationery as well.
I am open to color schemes, but perhaps something in purple tones.

Target Market(s)

Corporate clients

Industry/Entity Type

It Professional

Logo Text

Orbly IT

Number of Pages Required

1 page

Font styles to use
Other font styles liked:
• Eurostyle, Futura

Colors

Designer to choose colors to be used in the design.

Requirements
Must have
• Simple, streamlined look, but should not look too basic.

```html
<!DOCTYPE html>
<html lang="en">
<head>
<meta charset="utf-8">
<title>Orbly IT</title>
<link href="https://fonts.googleapis.com/css2?family=Jost:wght@400;500&family=Roboto:wght@400;500;700&family=Roboto+Condensed:wght@400;700&display=swap" rel="stylesheet">
<style>
:root{
  --purple:#4b1d6e;
  --crimson:#8e1537;
  --royal:#2418a8;
  --royal-deep:#170c78;
  --navy:#1c1878;
  --ink:#1e1e24;
  --text:#333;
  --muted:#555;
  --footer:#0d0d12;
  --white:#fff;
  --line:#8a8a8a;
}
*{box-sizing:border-box;margin:0;padding:0}
html,body{width:1200px;height:4091px;overflow:hidden;background:var(--white)}
body{position:relative;font-family:"Roboto",Arial,sans-serif;color:var(--text)}
section,header,footer{position:absolute;left:0;width:1200px}
.abs{position:absolute}
.topbar{top:0;height:11px;background:var(--purple)}
.site-header{top:11px;height:144px;background:var(--white)}
.brand{position:absolute;display:flex;align-items:center;gap:14px;font-family:"Roboto Condensed",sans-serif;font-weight:700;letter-spacing:1px}
.brand .mark{width:22px;height:22px;background:currentColor}
.site-header .brand{left:155px;top:42px;font-size:40px;color:var(--navy)}
.contact-line{position:absolute;left:808px;top:36px;font-size:19px;color:var(--ink);display:flex;align-items:center;gap:8px}
.header-icons{position:absolute;left:990px;top:38px;display:flex;gap:22px}
.nav{position:absolute;top:78px;left:423px;display:flex;font-size:20px;color:var(--ink)}
.nav a{position:absolute;white-space:nowrap;color:inherit;text-decoration:none}
.hero{top:155px;height:565px;background:radial-gradient(ellipse at 70% 40%,#3a2a30 0%,#1a1418 45%,#0e0c10 100%)}
.hero-media{position:absolute;left:630px;top:60px;width:480px;height:320px;border-radius:10px;background:linear-gradient(135deg,#5a5c63,#2a2b30 60%,#6b1424);opacity:.85}
.hero h1{position:absolute;left:161px;top:135px;font-family:"Roboto Condensed",sans-serif;font-weight:700;font-size:80px;color:var(--white);line-height:1}
.hero .tagline{position:absolute;left:161px;top:220px;font-family:"Roboto Condensed",sans-serif;font-size:50px;line-height:66px;color:var(--white)}
.btn{position:absolute;display:flex;align-items:center;justify-content:center;background:var(--crimson);color:var(--white);font-size:19px;text-transform:uppercase}
.hero .btn{left:161px;top:363px;width:153px;height:44px}
.hero .arrows{position:absolute;left:158px;top:462px;color:var(--white);font-size:22px;letter-spacing:22px}
.wave{position:absolute;left:0;width:1200px;height:60px}
.badge{position:absolute;left:580px;width:40px;height:40px;border:4px solid var(--royal);border-radius:50%}
h2{font-family:"Jost",sans-serif;font-weight:400;font-size:46px;letter-spacing:1px;color:var(--ink)}
.about{top:720px;height:526px}
.about-frame{left:147px;top:106px;width:371px;height:279px;border:2px solid var(--royal)}
.about-photo{left:175px;top:134px;width:390px;height:291px;background:linear-gradient(160deg,#5a6270,#23262e 55%,#8a2b33);box-shadow:0 4px 14px rgba(0,0,0,.3)}
.about h2{position:absolute;left:600px;top:140px}
.about p{position:absolute;left:600px;top:203px;width:450px;font-size:14px;line-height:24.5px;color:var(--muted)}
.about .btn{left:600px;top:393px;width:110px;height:33px;font-size:14px;text-transform:none}
.team{top:1246px;height:709px;background:linear-gradient(135deg,var(--royal) 0%,var(--royal-deep) 100%)}
.team h2{position:absolute;width:100%;text-align:center;top:97px;color:var(--white)}
.team .intro{position:absolute;left:250px;width:700px;top:168px;text-align:center;color:var(--white);font-size:14px;line-height:24px}
.member{position:absolute;top:306px;width:279px;height:289px;background:var(--white);padding:11px}
.member .photo{width:257px;height:230px;background:linear-gradient(180deg,#9aa2ad,#5d6f8a)}
.member .name{text-align:center;font-size:21px;color:var(--ink);margin-top:14px}
.products{top:1955px;height:799px}
.products h2{position:absolute;width:100%;text-align:center;top:111px}
.products .intro{position:absolute;left:200px;width:800px;top:188px;text-align:center;font-size:14px;line-height:27px;color:var(--muted)}
.group-label{position:absolute;width:100%;text-align:center;font-family:"Jost",sans-serif;font-size:30px;color:var(--ink)}
.bracket{position:absolute;left:224px;width:752px;height:40px;border:2px solid var(--line);border-bottom:none}
.bracket-gap{position:absolute;left:520px;width:160px;height:6px;background:var(--white)}
.partner{position:absolute;width:164px;height:88px;background:var(--white);box-shadow:0 2px 10px rgba(0,0,0,.18);display:flex;align-items:center;justify-content:center;font-family:"Roboto",sans-serif;font-weight:700;font-size:22px;color:var(--navy)}
.services{top:2754px;height:535px;background:linear-gradient(100deg,#4a1470 0%,#6a1a6e 50%,#8b1a4e 100%)}
.services h2{position:absolute;left:155px;top:155px;color:var(--white)}
.services p{position:absolute;left:155px;top:227px;width:445px;font-size:14px;line-height:27px;color:var(--white)}
.services-frame{left:649px;top:101px;width:393px;height:295px;border:2px solid rgba(255,255,255,.8)}
.services-card{left:627px;top:131px;width:393px;height:292px;background:var(--white);padding:10px}
.services-card .media{width:100%;height:100%;background:linear-gradient(160deg,#c9ccd1,#8d939c 50%,#1f7f8a)}
.newsletter{top:3289px;height:401px}
.newsletter h2{position:absolute;width:100%;text-align:center;top:98px}
.newsletter .sub{position:absolute;width:100%;text-align:center;top:155px;font-size:18px;color:var(--ink)}
.signup{position:absolute;left:202px;top:237px;width:796px;height:71px;display:flex;box-shadow:0 2px 8px rgba(0,0,0,.2)}
.signup .field{flex:1;border:1px solid #aaa;display:flex;align-items:center;padding-left:26px;font-size:19px;color:var(--ink)}
.signup .submit{width:142px;background:var(--royal-deep);color:var(--white);font-size:21px;display:flex;align-items:center;justify-content:center}
.site-footer{top:3690px;height:401px;background:var(--footer);color:var(--white)}
.site-footer .brand{left:155px;top:150px;font-size:40px;color:var(--white)}
.footer-col h3{position:absolute;font-family:"Roboto",sans-serif;font-weight:400;font-size:16px;letter-spacing:.5px}
.info{position:absolute;font-size:12px;line-height:18px;display:flex;gap:18px}
.links{position:absolute;left:764px;top:135px;list-style:none;font-size:12px;line-height:22px}
.links li::before{content:"•";margin-right:10px}
.social{position:absolute;left:949px;font-size:14px;display:flex;align-items:center;gap:10px}
.social span.dot{width:22px;height:22px;border:1.5px solid var(--white);border-radius:50%}
.copyright{position:absolute;width:100%;text-align:center;top:345px;font-size:12px}
</style>
</head>
<body>
<div class="topbar abs"></div>

<header class="site-header">
  <div class="brand"><span class="mark"></span>ORBLY IT</div>
  <div class="contact-line">
    <svg width="16" height="16" viewBox="0 0 24 24"><path fill="#8e1537" d="M6.6 10.8a15 15 0 006.6 6.6l2.2-2.2c.3-.3.7-.4 1-.2 1.1.4 2.3.6 3.6.6.6 0 1 .4 1 1V20c0 .6-.4 1-1 1A17 17 0 013 4c0-.6.4-1 1-1h3.5c.6 0 1 .4 1 1 0 1.3.2 2.5.6 3.6.1.3 0 .7-.2 1z"/></svg>
    905-555-0147
  </div>
  <div class="header-icons">
    <svg width="17" height="17" viewBox="0 0 24 24"><circle cx="10" cy="10" r="7" fill="none" stroke="#1e1e24" stroke-width="3"/><path d="M15 15l7 7" stroke="#1e1e24" stroke-width="3"/></svg>
    <svg width="17" height="17" viewBox="0 0 24 24"><circle cx="12" cy="7" r="5" fill="#1e1e24"/><path d="M2 23c0-6 4-9 10-9s10 3 10 9z" fill="#1e1e24"/></svg>
  </div>
  <nav class="nav">
    <a style="left:0">Home</a>
    <a style="left:92px">About Us</a>
    <a style="left:210px">Our Team</a>
    <a style="left:327px">Products</a>
    <a style="left:444px">Services</a>
    <a style="left:556px">Contact</a>
  </nav>
</header>

<section class="hero">
  <div class="hero-media" role="img" aria-label="Stack of solid state drives"></div>
  <h1>ORBLY IT</h1>
  <div class="tagline">Hard Disk Drives<br>and Solid State Drives.</div>
  <div class="btn">View More</div>
  <div class="arrows">‹ ›</div>
  <svg class="wave" style="top:505px" viewBox="0 0 1200 60" preserveAspectRatio="none"><path d="M0 60 L0 52 L480 52 C540 52 550 0 600 0 C650 0 660 52 720 52 L1200 52 L1200 60 Z" fill="#fff"/></svg>
  <div class="badge" style="top:545px"></div>
</section>

<section class="about">
  <div class="abs about-frame"></div>
  <div class="abs about-photo" role="img" aria-label="Technician working in a server room aisle, video preview"></div>
  <svg class="abs" style="left:342px;top:251px" width="56" height="56" viewBox="0 0 56 56"><circle cx="28" cy="28" r="26" fill="rgba(0,0,0,.45)" stroke="#fff" stroke-width="2"/><path d="M22 17 L40 28 L22 39 Z" fill="#fff"/></svg>
  <h2>ABOUT US</h2>
  <p>We are a specialized IT trading company, with a focus on high end storage solutions. As businesses and individuals continue to generate ever-greater amounts of data, storage technologies need to keep pace. We believe that understanding the needs of our customers puts us in an excellent position to fulfill their requirements in this fast evolving market. We operate in the Middle East, Africa and the CIS, and are particularly well suited to the complex dynamics of these markets.</p>
  <div class="btn">Read More</div>
</section>

<section class="team">
  <h2>OUR TEAM</h2>
  <p class="intro">Our team is here to serve you. All of our sales professionals and technical support staff have a passion for information technology, and are dedicated to our customers. Our management team comprises individuals with many years of in-depth experience in the storage solutions sector.</p>
  <div class="member" style="left:155px"><div class="photo" role="img" aria-label="Portrait of team member"></div><div class="name">Porro quisquam</div></div>
  <div class="member" style="left:464px"><div class="photo" role="img" aria-label="Portrait of team member"></div><div class="name">Dolorem ipsum</div></div>
  <div class="member" style="left:766px"><div class="photo" role="img" aria-label="Portrait of team member"></div><div class="name">Quisquam est qui</div></div>
  <svg class="wave" style="top:649px" viewBox="0 0 1200 60" preserveAspectRatio="none"><path d="M0 60 L0 52 L480 52 C540 52 550 0 600 0 C650 0 660 52 720 52 L1200 52 L1200 60 Z" fill="#fff"/></svg>
  <div class="badge" style="top:689px"></div>
</section>

<section class="products">
  <h2>PRODUCTS</h2>
  <p class="intro">As a high end storage specialist, we trade in memory, as well as Hard Disk Drives and Solid State Drives. Whether it be mass market product ranges, or specialized products, we will be able to source and deliver at the most competitive price.</p>
  <div class="bracket" style="top:298px"></div><div class="bracket-gap" style="top:296px"></div>
  <div class="group-label" style="top:278px">Memory</div>
  <div class="partner" style="left:155px;top:344px">NORVANE</div>
  <div class="partner" style="left:335px;top:344px">memtrix</div>
  <div class="partner" style="left:515px;top:344px">Kellon</div>
  <div class="partner" style="left:695px;top:344px">Stratum</div>
  <div class="partner" style="left:875px;top:344px">VELKOR</div>
  <div class="bracket" style="top:508px"></div><div class="bracket-gap" style="top:506px"></div>
  <div class="group-label" style="top:488px">Storage</div>
  <div class="partner" style="left:155px;top:551px">Quarryline</div>
  <div class="partner" style="left:335px;top:551px">Tidecell</div>
  <div class="partner" style="left:515px;top:551px">ARKADA</div>
  <div class="partner" style="left:695px;top:551px">HOSHIRO</div>
  <div class="partner" style="left:875px;top:551px">FENMARK</div>
</section>

<section class="services">
  <h2>SERVICES</h2>
  <p>We are first and foremost a trusted supplier of storage products. In this respect, our strong technical expertise and wide range of experience allows us to consult clients on the best strategy for meeting their data storage needs, coupled with a clear commitment for delivering the products required to execute this. We work with blanket orders as required, giving customers the possibility to secure stock and plan ahead without the worry of product shortages or price fluctuations.</p>
  <div class="abs services-frame"></div>
  <div class="abs services-card"><div class="media" role="img" aria-label="Exploded view of a solid state drive"></div></div>
  <svg class="wave" style="top:475px" viewBox="0 0 1200 60" preserveAspectRatio="none"><path d="M0 60 L0 52 L480 52 C540 52 550 0 600 0 C650 0 660 52 720 52 L1200 52 L1200 60 Z" fill="#fff"/></svg>
  <div class="badge" style="top:515px"></div>
</section>

<section class="newsletter">
  <h2>NEWSLETTER</h2>
  <p class="sub">Neque porro quisquam est qui dolorem ipsum quia dolor sit amet</p>
  <div class="signup"><div class="field">Email id</div><div class="submit">Subscribe</div></div>
</section>

<footer class="site-footer">
  <div class="brand"><span class="mark"></span>ORBLY IT</div>
  <div class="footer-col">
    <h3 style="left:469px;top:90px">CONTACT US</h3>
    <div class="info" style="left:469px;top:138px">
      <svg width="14" height="18" viewBox="0 0 24 32"><path d="M12 0a10 10 0 00-10 10c0 8 10 22 10 22s10-14 10-22A10 10 0 0012 0zm0 14a4 4 0 110-8 4 4 0 010 8z" fill="#fff"/></svg>
      <span>Harbor Point Business Park<br>Coral Bay District</span>
    </div>
    <div class="info" style="left:469px;top:196px">
      <svg width="14" height="14" viewBox="0 0 24 24"><path fill="#fff" d="M6.6 10.8a15 15 0 006.6 6.6l2.2-2.2c.3-.3.7-.4 1-.2 1.1.4 2.3.6 3.6.6.6 0 1 .4 1 1V20c0 .6-.4 1-1 1A17 17 0 013 4c0-.6.4-1 1-1h3.5c.6 0 1 .4 1 1 0 1.3.2 2.5.6 3.6.1.3 0 .7-.2 1z"/></svg>
      <span>+00 8 5550 1100<br>+00 8 5550 1300</span>
    </div>
    <div class="info" style="left:469px;top:247px">
      <svg width="14" height="12" viewBox="0 0 24 18"><rect width="24" height="18" fill="#fff"/><path d="M0 0 L12 10 L24 0" fill="none" stroke="#0d0d12" stroke-width="2"/></svg>
      <span>contact@orblyit.me</span>
    </div>
    <h3 style="left:764px;top:90px">QUICK LINKS</h3>
    <ul class="links"><li>Home</li><li>About Us</li><li>Our Team</li><li>Products</li><li>Services</li><li>Contact Us</li></ul>
    <h3 style="left:949px;top:90px">FOLLOW US</h3>
    <div class="social" style="top:135px"><span class="dot"></span>Linkbook</div>
    <div class="social" style="top:176px"><span class="dot"></span>Snapgrid</div>
    <div class="social" style="top:217px"><span class="dot"></span>Circles+</div>
  </div>
  <p class="copyright">© Copyright 2019 . All Rights Reserved.</p>
</footer>
</body>
</html>
```